Flyer Design Project for Harbourline Janitorial Group Inc.

We require a double sided marketing flyer 8 1/2 x 11. The flyer will also be marketed via e-mail using one or both sides. "Outside of the box" but yet "professional" marketing is what we'd like to achieve.

Harbourline Janitorial Group Inc., is a building service company providing cleaning, caretaking and concierge service to residential/stratas (condominiums/apartments)...(These services are usually provided during daytime hours). and janitorial service to commercial buildings ( service provided at night time).

- 100% green cleaning chemicals and systems
- Professionally trained staff
- Customer service is #1 priority
- Excellent Communication systems

Brochure to be 2 pages.:

Side 1: marketing residential/strata building services with a focus on providing cleaning services with a sub-focus on caretaking and concierge. We also provide move-in/out service where we coordinate with tenants to arrange access to the building, elevators and provide security (no moving involved)

Side 2: marketing night time janitorial service to property managers, corporate head offices, small offices, industrial facilities

http://www.tidy-nest-example.com/index.php

http://www.brightkeepwest.example/services

These websites are from the best maid cleaning business and best strata//residential cleaning business in the city. The maid website is "you" focused, that works! The other is very straight forward and to the point, which also works.

At the end of the day our target audience ( property managers and building owners ) want us to take away one of their biggest headaches - "CLEANING". They have better things to be doing than dealing with whether or not the elevator is clean! That's our job! We're in the CLEANING business and when they don't hear a word from any of their tenants, we're doing our job and they're HAPPY :) WE TAKE AWAY HEADACHES AND MAKE PEOPLE HAPPY!

very multi-cultural target audience!

HOW CAN WE SHOW THEM IN A FLYER? THAT'S THE CHALLENGE! AND THE WINNING DESIGNER WILL BE THE ONE WHO CAN EFFECTIVELY COMMUNICATE THIS IN 1-2 PAGES.
Updates

Thank you all very much. Verolinda and Quill, your designs are very encouraging.

Design 1223617: The layout is close to what we are hoping to achieve as it may also be incorporated into a web site homepage with each block used as a link to more info. The pictures however, make it look like any other company flyer.

Design 1224020: Also a very good layout but again not liking the pictures.

Overall, some of the designs are a little to busy with information. I would like to see something just a little more simple and yet unique that stands out against other companies.

Look forward to the second round. Thank you all very much!

Please see the new files called commercial building pics, residential strata pics and misc pics that you can use in the brochure. These are the types of pictures I would like included. Thanks.

Hi Designers

Would like to see a design that combines the layout format of the bottom half of 1234602 ( easy to read) and the top half of 1227356 ( like the pictures in this one).

Also, want to replace "Marketing....." with Side #1 " Providing residential/stratas with quality, affordable cleaning, caretaking and concierge services.. and then the rest of the text in point/bullet form.

With side #2, want to replace " Marketing...." with "Providing quality, affordable commercial janitorial service to....

                                   

 

Please use latest pictures uploaded. The designs we've liked so far have 1 large picture ( picture of buildings ) on each side with 2-3 smaller pics in various layouts. i.e. for side 1 : Cleaning ( a picture of a cleaner ) Caretaking ( picture of handyman in white shaking hand) Concierge ( picture of person at a desk on the phone)

The font should be large and easy to read. We also like the designs where key points are in point form.

The company name and logo and contact info should be easy to read.

We did like one design using vector characters but think they should only be incorporated as part of the overall design

Target Market(s)

Property Managers, Building Owners, Multicultural Decision makers, aged 28 - 60, very busy people

Industry/Entity Type

Janitorial Service

Requirements
Must have
• 2 pages, 8 1/2 x 11 ( double sided) but can be used separately
Nice to have
• Would like to be able to change photos for different campaigns

```html
<!DOCTYPE html>
<html lang="en">
<head>
<meta charset="utf-8">
<title>Harbourline Janitorial Group – Residential Flyer</title>
<link rel="stylesheet" href="https://fonts.googleapis.com/css2?family=Open+Sans:wght@400;600;700;800&display=swap">
<style>
  :root{
    --green:#8cc63f;
    --green-dark:#5e9a1e;
    --green-light:#b9e07a;
    --ink:#4a4a4a;
    --ink-dark:#222;
    --paper:#ffffff;
    --frame:#b8bcc0;
    --sky:#7fa6cf;
    --sky-deep:#3e6b9c;
  }
  *{box-sizing:border-box;margin:0;padding:0}
  html,body{width:983px;height:1200px;overflow:hidden;background:var(--paper)}
  body{font-family:"Open Sans",Arial,sans-serif}
  .flyer{position:relative;width:983px;height:1200px;overflow:hidden;background:var(--paper)}

  .corner-accent{position:absolute;left:0;top:0}
  .logo-band{position:absolute;left:0;top:0}

  .photo{position:absolute;border-radius:22px;transform:rotate(45deg);overflow:hidden;
    box-shadow:0 6px 14px rgba(0,0,0,.25)}
  .photo--window{left:96px;top:72px;width:290px;height:290px;
    background:linear-gradient(135deg,#c9dff2 0%,var(--sky) 45%,var(--sky-deep) 100%)}
  .photo--climbers{left:585px;top:395px;width:370px;height:370px;
    background:linear-gradient(160deg,#dde3ec 0%,#a9b7cb 50%,#5d6f88 100%)}

  .tile{position:absolute;border-radius:16px;border:8px solid var(--frame);
    background:radial-gradient(circle at 35% 35%,var(--green-light),var(--green) 45%,var(--green-dark) 100%);
    box-shadow:0 4px 10px rgba(0,0,0,.3)}
  .tile--a{left:-60px;top:560px;width:150px;height:150px;transform:rotate(-35deg)}
  .tile--b{left:-10px;top:760px;width:170px;height:170px;transform:rotate(-28deg)}
  .tile--c{left:-70px;top:1080px;width:170px;height:150px;transform:rotate(-28deg)}
  .tile--d{left:915px;top:900px;width:120px;height:130px;transform:rotate(-30deg)}

  .brand{position:absolute;left:560px;top:150px;display:flex;align-items:center;gap:14px}
  .brand__dot{width:22px;height:22px;border-radius:50%;background:var(--green)}
  .brand__name{font-weight:600;font-size:60px;color:var(--ink-dark);letter-spacing:-1px;line-height:1}

  .services-head{position:absolute;font-weight:800;font-size:31px;color:var(--ink);letter-spacing:.5px;line-height:1}
  .services-head--1{left:427px;top:332px}
  .services-head--2{left:358px;top:372px}
  .services-head--3{left:290px;top:412px}

  .point{position:absolute;height:48px;background:var(--green);color:#fff;font-weight:700;
    font-size:15.5px;line-height:1.15;display:flex;flex-direction:column;justify-content:center;
    padding-left:48px;clip-path:polygon(0 0,100% 0,100% 100%,22px 100%);
    filter:drop-shadow(0 6px 5px rgba(0,0,0,.3))}
  .point--1{left:32px;top:459px;width:432px}
  .point--2{left:65px;top:517px;width:440px}
  .point--3{left:102px;top:578px;width:440px;padding-left:110px}
  .point--4{left:143px;top:643px;width:441px;padding-left:60px}
  .point--5{left:191px;top:706px;width:434px;padding-left:60px}
  .point small{font-size:15.5px;font-weight:700}
  .point em{font-style:normal;padding-left:90px}

  .service-title{position:absolute;left:223px;top:790px;font-weight:800;font-size:38px;color:var(--ink)}
  .service-line{position:absolute;font-size:20px;color:var(--green);font-weight:400;white-space:nowrap}

  .move-note{position:absolute;left:126px;top:1030px;font-weight:800;font-size:17px;line-height:1.25;color:var(--ink-dark)}

  .contact-panel{position:absolute;left:500px;top:960px;width:720px;height:470px;border-radius:40px;
    border:12px solid #d5d8db;transform:rotate(-27deg);
    background:linear-gradient(160deg,var(--green-light) 0%,var(--green) 40%,var(--green-dark) 100%)}
  .contact{position:absolute;right:18px;top:1046px;text-align:right;color:#fff}
  .contact__company{font-size:23px;font-weight:400;margin-bottom:6px}
  .contact__address{font-size:13px;line-height:1.7;padding-right:60px}
  .contact__phone{font-size:27px;font-weight:400;margin-top:6px}
  .contact__email{font-size:23px;font-weight:400}
</style>
</head>
<body>
<main class="flyer">
  <svg class="corner-accent" width="983" height="520" viewBox="0 0 983 520" aria-hidden="true">
    <polygon points="0,0 190,0 0,300" fill="var(--green)"/>
    <polygon points="120,220 390,300 220,300" fill="var(--green)"/>
    <polygon points="500,258 983,258 983,290 540,290 620,274" fill="var(--green)"/>
  </svg>

  <div class="tile tile--a" aria-hidden="true"></div>
  <div class="tile tile--b" aria-hidden="true"></div>
  <div class="tile tile--c" aria-hidden="true"></div>
  <div class="tile tile--d" aria-hidden="true"></div>

  <div class="photo photo--window" role="img" aria-label="Cleaner squeegeeing a soapy window"></div>

  <div class="brand">
    <span class="brand__dot"></span>
    <span class="brand__name">Harbourline</span>
  </div>

  <h1 class="services-head services-head--1">CLEANING</h1>
  <h2 class="services-head services-head--2">CARETAKING</h2>
  <h2 class="services-head services-head--3">CONCIERGE</h2>

  <div class="photo photo--climbers" role="img" aria-label="Rope-access window cleaners silhouetted on a glass tower"></div>

  <ul>
    <li class="point point--1"># 1 PRIORITY - CUSTOMER SERVICE<small>&nbsp;&nbsp;And communication</small></li>
    <li class="point point--2">OVER 20 YEARS INDUSTRY EXPERIENCE<br>TRAINED, COUTEOUS STAFF</li>
    <li class="point point--3">100% GREEN CHEMICALS</li>
    <li class="point point--4"><span style="font-style:italic;font-weight:600">Servicing greater vancouver</span>AFFORDABLE, QUALITY SERVICE</li>
    <li class="point point--5">NEW CONSTRUCTION?<em>WE DO MOVE-INS/OUST</em></li>
  </ul>

  <h2 class="service-title">Service</h2>
  <p class="service-line" style="left:348px;top:840px">Daily, weekly, monthly and yearly cleaning services</p>
  <p class="service-line" style="left:318px;top:866px">Initial cleaning / one-time jobs</p>
  <p class="service-line" style="left:271px;top:893px">Project work / all types of floor maintenance</p>
  <p class="service-line" style="left:226px;top:920px">Caretaker and building management services</p>
  <p class="service-line" style="left:196px;top:947px">Monthly building reports and audits</p>

  <p class="move-note">NEW CONSTRUCTION?<br>WE DO MOVE-INS/OUTS</p>

  <div class="contact-panel" aria-hidden="true"></div>
  <address class="contact" style="font-style:normal">
    <p class="contact__company">Harbourline Janitorial Group Inc.</p>
    <p class="contact__address">1234, street Name, State Name,<br>Country Name, Country Name,</p>
    <p class="contact__phone">CALL 604-555-0142</p>
    <p class="contact__email">E: dana@harbourlinejg.com</p>
  </address>
</main>
</body>
</html>
```